Bold Cover needed for a book on Workplace Bullying

I need a book cover design for a book titled, “Iron Silence?” The book recounts my story of bullying in the workplace. It also includes chapters on how readers can minimize/stop workplace bullying, write an effective complaint, and ensure their own mental wellbeing.
I am looking for a bold design using red and black, and possibly distressed lettering. The covers of other books dealing with this subject do not reflect my vision. They are often too childish or look too academic. This book needs to stress the serious nature of a toxic workplace, while appealing to readers experiencing a similar situation. I’d like the cover to reflect the mental anguish associated with workplace bullying (hence the distressed lettering).
I have included a cover that appeals to me (although the coloring is wrong). That said, I am also very happy (and excited) to see your creative input!
On the cover, it should have the following:
Title: Iron Silence?
Subtitle: How the Harbour Works Department Condones Bullying & Ruins Lives
Author: Owen Frick
Other relevant details:
Book size: 5.5” x 8.5”
Back cover will have a blurb, author picture/short bio, and barcode
The blurb on the back cover reads:
Undermining, intimidation and threats
Despite the Department of Harbour Works allegedly holding a Iron Silence for bullying, these behaviours were an everyday occurrence in at least one workplace. Even after a decade of complaints, numerous witnesses and physical proof, the department failed to act. Instead, they looked the other way, allowing one powerful and well-connected individual to end careers and ruin lives.
After being targeted, one teacher resolved to put an end to the abuse experienced by more than fifty employees. His startling story reveals the relentless bullying, mental health ramifications, and insidious tactics used to cover up the corrosive behaviour.
Those who have experienced a toxic workplace will also find much needed support and guidance, intended to minimise suffering and detail a clear way forward. Chapters include dealing with bullying in the workplace, how to lodge a successful complaint, and how to stay sane during any potential legal action.

```html
<!DOCTYPE html>
<html lang="en">
<head>
<meta charset="utf-8">
<title>Iron Silence — Owen Frick — Book Cover</title>
<link rel="stylesheet" href="https://fonts.googleapis.com/css2?family=Barlow+Semi+Condensed:wght@600&family=Saira+Stencil+One&family=Open+Sans:wght@600&family=Jost:wght@500&display=swap">
<style>
  :root {
    --backdrop: #dededc;
    --navy: #16264d;
    --navy-edge: #101d3d;
    --orange: #f06b1c;
    --title-white: #f2f1ec;
    --subtitle-yellow: #ecd60e;
    --soft-shadow: rgba(20, 20, 20, 0.35);
  }
  html, body {
    margin: 0;
    padding: 0;
    width: 1200px;
    height: 1013px;
    overflow: hidden;
    background: var(--backdrop);
  }
  .stage {
    width: 1200px;
    height: 1013px;
    display: flex;
    align-items: center;
    justify-content: center;
  }
  .book-cover {
    width: 666px;
    height: 940px;
    display: block;
  }
  .panel-navy { fill: var(--navy); }
  .panel-orange { fill: var(--orange); }
  .spine-fold { stroke: var(--navy-edge); stroke-width: 3; }
  .title-main {
    font-family: "Barlow Semi Condensed", "Arial Narrow", sans-serif;
    font-weight: 600;
    font-size: 292px;
    fill: var(--title-white);
    filter: drop-shadow(2px 2px 0 var(--soft-shadow));
  }
  .title-worn {
    font-family: "Saira Stencil One", "Impact", sans-serif;
    font-size: 168px;
    fill: var(--title-white);
  }
  .subtitle {
    font-family: "Open Sans", "Helvetica", sans-serif;
    font-weight: 600;
    font-size: 29px;
    fill: var(--subtitle-yellow);
    filter: drop-shadow(1.5px 1.5px 0 var(--soft-shadow));
  }
  .author {
    font-family: "Jost", "Futura", sans-serif;
    font-weight: 500;
    font-size: 90px;
    fill: var(--title-white);
    filter: drop-shadow(2px 2px 0 var(--soft-shadow));
  }
</style>
</head>
<body>
<main class="stage">
  <svg class="book-cover" viewBox="0 0 885 1250" xmlns="http://www.w3.org/2000/svg" aria-labelledby="cover-title">
    <title id="cover-title">Iron Silence — How the Harbour Works Department Condones Bullying &amp; Ruins Lives — Owen Frick</title>
    <defs>
      <filter id="worn-ink" x="-5%" y="-10%" width="110%" height="120%">
        <feTurbulence type="fractalNoise" baseFrequency="0.09" numOctaves="3" seed="7" result="grain"/>
        <feColorMatrix in="grain" type="matrix"
          values="0 0 0 0 0  0 0 0 0 0  0 0 0 0 0  0 0 0 -3 2.15" result="grain-mask"/>
        <feComposite in="SourceGraphic" in2="grain-mask" operator="in"/>
      </filter>
    </defs>

    <rect class="panel-orange" x="0" y="0" width="885" height="1250"/>
    <rect class="panel-navy" x="0" y="0" width="236" height="1250"/>
    <line class="spine-fold" x1="43" y1="0" x2="43" y2="1250"/>

    <text class="title-main" x="446" y="352" text-anchor="middle" textLength="630" lengthAdjust="spacing">IRON</text>
    <text class="title-worn" x="443" y="510" text-anchor="middle" textLength="640" lengthAdjust="spacing" filter="url(#worn-ink)">SILENCE</text>

    <text class="subtitle" x="465" y="1010" text-anchor="middle">HOW THE HARBOUR WORKS DEPARTMENT CONDONES</text>
    <text class="subtitle" x="465" y="1050" text-anchor="middle">BULLYING &amp; RUINS LIVES</text>

    <text class="author" x="440" y="1182" text-anchor="middle">OWEN FRICK</text>
  </svg>
</main>
</body>
</html>
```